Personal training poster

Hi, I need a poster designed for my personal training business to help attracted some new clients over these quiet months. I want the poster to be eye catching and something that I can put up in the gym when I need to attract some new business, so it can no be seasional (i.e) Winter, Summer reference.

My logo has to be includes (Calloway Strength & Nutrition)

Target Market(s)

New clients within a gym envitoment

Industry/Entity Type

Fitness

Font styles to use
Serif

Colors

Designer to choose colors to be used in the design.

Requirements
Must have
• My Logo
• Personal training introductory offer 4 X 45min sessions $180
• STOP WISHING. START DOING.
• Want to loose weight and or build muscle?
• Want to feel healthier and fitter
• Want to learn proper/safe techique?
• Please contact Dale @ callowaystrength@examplemail.net or phone 0472815094
• *conditions apply at the bottom
Nice to have
• My facebook and instagram
• calloway_strength_nutrition (instagram)
• Calloway Strength & Nutrition (facebook)
• Eat Clean, Train Dirty
Should not have
• Imiges of Femaile trainers as I am a Male

```html
<!DOCTYPE html>
<html lang="en">
<head>
<meta charset="utf-8">
<title>Calloway Strength &amp; Nutrition – Personal Training</title>
<link href="https://fonts.googleapis.com/css2?family=Oswald:wght@400;500;600&family=Raleway:wght@300;400&family=Michroma&family=Questrial&family=Arimo&family=Rasa:wght@500&display=swap" rel="stylesheet">
<style>
  :root {
    --ink: #0b0b0c;
    --white: #ffffff;
    --muted: #b8b8b8;
    --blue: #12b3ea;
    --red: #e3141c;
    --band: rgba(40, 40, 42, 0.72);
  }
  html, body {
    margin: 0;
    padding: 0;
    overflow: hidden;
    background: var(--ink);
  }
  .poster {
    position: relative;
    width: 846px;
    height: 1200px;
    overflow: hidden;
    background: var(--ink);
    color: var(--white);
  }
  .poster-photo {
    position: absolute;
    inset: 0;
    background:
      radial-gradient(ellipse 70% 40% at 85% 8%, #f4f4f4 0%, #b9b9b9 35%, rgba(90,90,90,0) 75%),
      radial-gradient(ellipse 60% 45% at 80% 80%, #6e6e70 0%, rgba(40,40,40,0) 70%),
      linear-gradient(160deg, #1a1a1b 0%, #3b3b3d 45%, #202022 70%, #0d0d0e 100%);
  }
  .headline {
    position: absolute;
    left: 44px;
    margin: 0;
    font-family: "Oswald", sans-serif;
    font-weight: 500;
    font-size: 76px;
    line-height: 1;
    letter-spacing: 9px;
  }
  .headline-personal { top: 64px; color: var(--white); }
  .headline-training { top: 138px; color: var(--blue); }
  .offer {
    position: absolute;
    left: 58px;
    top: 226px;
    font-family: "Raleway", sans-serif;
    font-weight: 300;
  }
  .offer-label { color: var(--red); font-size: 45px; line-height: 1; margin: 0; }
  .offer-sessions { font-size: 39px; line-height: 1; margin: 6px 0 0 4px; font-weight: 400; }
  .offer-price {
    position: absolute;
    left: 87px;
    top: 314px;
    font-family: "Raleway", sans-serif;
    font-weight: 300;
    margin: 0;
    display: flex;
    align-items: flex-start;
  }
  .offer-price-for { font-size: 34px; margin-top: 14px; font-weight: 400; }
  .offer-price-amount { font-size: 92px; line-height: 1; color: var(--red); margin-left: 14px; letter-spacing: -2px; }
  .motto {
    position: absolute;
    left: 344px;
    top: 450px;
    margin: 0;
    font-family: "Michroma", sans-serif;
    font-weight: 400;
    font-size: 37px;
    line-height: 43px;
    letter-spacing: 2.6px;
  }
  .motto-rule {
    position: absolute;
    left: 347px;
    top: 544px;
    width: 437px;
    height: 5px;
    background: var(--blue);
  }
  .goals {
    position: absolute;
    right: 56px;
    top: 566px;
    margin: 0;
    padding: 0;
    list-style: none;
    font-family: "Oswald", sans-serif;
    font-weight: 600;
    font-size: 23px;
    text-align: right;
  }
  .goal {
    display: flex;
    justify-content: flex-end;
    align-items: center;
    height: 35px;
  }
  .goal-tick { width: 44px; height: 34px; margin-left: 14px; }
  .slogan-band {
    position: absolute;
    left: 0;
    top: 730px;
    width: 846px;
    height: 78px;
    background: linear-gradient(90deg, rgba(40,40,42,0.4) 0%, var(--band) 20%, var(--band) 80%, rgba(40,40,42,0.3) 100%);
  }
  .slogan {
    position: absolute;
    left: 153px;
    top: 732px;
    margin: 0;
    font-family: "Questrial", sans-serif;
    font-size: 62px;
    line-height: 70px;
    white-space: nowrap;
  }
  .slogan-accent { color: var(--blue); }
  .contact {
    position: absolute;
    left: 0;
    right: 0;
    top: 862px;
    margin: 0;
    text-align: center;
    font-family: "Arimo", sans-serif;
    font-size: 26px;
    line-height: 36px;
    letter-spacing: -0.6px;
  }
  .brand {
    position: absolute;
    left: 0;
    right: 0;
    top: 1000px;
    margin: 0;
    text-align: center;
    font-family: "Oswald", sans-serif;
    font-weight: 500;
    color: var(--white);
    font-size: 40px;
    line-height: 50px;
    letter-spacing: 4px;
  }
  .socials {
    position: absolute;
    left: 48px;
    right: 22px;
    top: 1141px;
    display: flex;
    justify-content: space-between;
    font-family: "Rasa", serif;
    font-weight: 500;
    font-size: 22px;
    line-height: 26px;
  }
  .social { display: flex; align-items: center; }
  .social-mark {
    width: 20px;
    height: 20px;
    background: var(--white);
    border-radius: 3px;
    margin-right: 10px;
  }
  .conditions {
    position: absolute;
    left: 0;
    right: 0;
    top: 1176px;
    margin: 0;
    text-align: center;
    font-family: "Arimo", sans-serif;
    font-size: 12px;
    line-height: 16px;
    color: var(--muted);
  }
</style>
</head>
<body>
<main class="poster">
  <div class="poster-photo" role="img" aria-label="Black and white gym photograph: an athlete holding a core exercise above rows of dumbbells on a rack"></div>

  <h1 class="headline headline-personal">PERSONAL</h1>
  <h1 class="headline headline-training">TRAINING</h1>

  <div class="offer">
    <p class="offer-label">introductory offer</p>
    <p class="offer-sessions">4 X 45min sessions</p>
  </div>
  <p class="offer-price">
    <span class="offer-price-for">FOR</span>
    <span class="offer-price-amount">$180</span>
  </p>

  <h2 class="motto">STOP WISHING.<br>START.DOING.</h2>
  <div class="motto-rule"></div>

  <ul class="goals">
    <li class="goal">WANT TO LOOSE WEIGHT AND OR BUILD MUSCLE?
      <svg class="goal-tick" viewBox="0 0 44 34" aria-hidden="true"><rect x="8" y="16" width="15" height="15" fill="#12b3ea"/><path d="M6 18 L16 28 L42 2" fill="none" stroke="#fff" stroke-width="3"/></svg></li>
    <li class="goal">WANT TO FEEL HEALTHIER AND FITTER
      <svg class="goal-tick" viewBox="0 0 44 34" aria-hidden="true"><rect x="8" y="16" width="15" height="15" fill="#12b3ea"/><path d="M6 18 L16 28 L42 2" fill="none" stroke="#fff" stroke-width="3"/></svg></li>
    <li class="goal">WANT TO LEARN PROPER/SAFE TECHIQUE?
      <svg class="goal-tick" viewBox="0 0 44 34" aria-hidden="true"><rect x="8" y="16" width="15" height="15" fill="#12b3ea"/><path d="M6 18 L16 28 L42 2" fill="none" stroke="#fff" stroke-width="3"/></svg></li>
  </ul>

  <div class="slogan-band"></div>
  <p class="slogan">Eat Clean, <span class="slogan-accent">Train Dirty</span></p>

  <p class="contact">Please contact Dale @<br>callowaystrength@examplemail.net or call 0472815094</p>

  <p class="brand">CALLOWAY<br>STRENGTH &amp; NUTRITION</p>

  <footer class="socials">
    <span class="social"><span class="social-mark"></span>Calloway Strength &amp; Nutrition</span>
    <span class="social"><span class="social-mark"></span>calloway_strength_nutrition</span>
  </footer>
  <p class="conditions">*conditions apply</p>
</main>
</body>
</html>
```